Newspaper ad for web design services

I have a paid space in a local newspaper size: 4.5085" W x 2.6875" H.
I want to use it for promoting my web design services.
Designers have the freedom to design the ad and the offer.
The goal is to have people contact me for business web design.
I published one ad last month and it totally failed to bring any attention.
Feel free to change or add anything you think can be more effective to attract potential customers (I can create any tripwire you consider will work)
Target: Houston-based business owners looking to get a new website or to update their existing one.

```html
<!DOCTYPE html>
<html lang="en">
<head>
<meta charset="utf-8">
<title>Nova Webworks – Free E-Book Newspaper Ad</title>
<link rel="stylesheet" href="https://fonts.googleapis.com/css2?family=Montserrat:wght@800;900&family=Mulish:ital,wght@0,500;0,600;1,800&display=swap">
<style>
  :root {
    --brand-blue: #3a5fb8;
    --ink: #0b0b0b;
    --paper: #ffffff;
    --paper-shade: #d9d9db;
    --night: #0e1222;
    --night-edge: #1b2236;
    --tick-green: #2fa836;
    --art-blue: #3f63c4;
    --art-red: #d7302d;
  }
  * { margin: 0; padding: 0; box-sizing: border-box; }
  html, body { width: 1200px; height: 658px; overflow: hidden; background: var(--paper); }
  .ad {
    position: relative;
    width: 1200px;
    height: 658px;
    overflow: hidden;
    font-family: "Mulish", sans-serif;
  }
  .ad__backdrop { position: absolute; inset: 0; }

  .offer { position: absolute; left: 53px; top: 0; }
  .offer__kicker {
    position: absolute; top: 58px; white-space: nowrap;
    font-size: 36px; font-weight: 600; color: var(--brand-blue); line-height: 1;
  }
  .offer__title {
    position: absolute; top: 98px; white-space: nowrap;
    font-family: "Montserrat", sans-serif; font-weight: 900;
    font-size: 42px; color: var(--ink); line-height: 1;
  }
  .pitch__lead {
    position: absolute; top: 198px; white-space: nowrap;
    font-size: 27px; font-weight: 600; color: var(--brand-blue); line-height: 1;
  }
  .pitch__headline {
    position: absolute; top: 232px; white-space: nowrap;
    font-family: "Montserrat", sans-serif; font-weight: 900;
    font-size: 46px; line-height: 44px; color: var(--ink);
  }
  .pitch__promise {
    position: absolute; top: 326px; white-space: nowrap;
    font-size: 30px; font-weight: 600; color: var(--brand-blue); line-height: 1;
  }
  .benefits {
    position: absolute; top: 408px; list-style: none;
  }
  .benefits__item {
    display: flex; align-items: center; gap: 10px;
    height: 51px; white-space: nowrap;
    font-size: 30px; font-weight: 800; font-style: italic; color: var(--brand-blue);
  }
  .benefits__tick { width: 36px; height: 30px; flex: none; }

  .brand {
    position: absolute; left: 765px; top: 44px;
    display: flex; align-items: center; gap: 16px;
  }
  .brand__square { width: 88px; height: 88px; background: var(--brand-blue); border-radius: 12px; }
  .brand__name {
    font-size: 50px; font-weight: 600; color: var(--paper); line-height: 46px;
  }
  .hero-art {
    position: absolute; left: 768px; top: 188px; width: 352px; height: 384px;
    border-radius: 18px;
    background: linear-gradient(150deg, var(--art-blue) 0%, #2b4596 55%, var(--art-red) 140%);
    opacity: .9;
  }
  .visit {
    position: absolute; left: 738px; top: 580px; white-space: nowrap;
    color: var(--paper); font-weight: 800; font-size: 26px;
  }
  .visit__label { font-size: 19px; font-weight: 600; }
</style>
</head>
<body>
<main class="ad">
  <svg class="ad__backdrop" width="1200" height="658" viewBox="0 0 1200 658" aria-hidden="true">
    <defs>
      <linearGradient id="nightFill" x1="0" y1="0" x2="1" y2="1">
        <stop offset="0" stop-color="var(--night-edge)"/>
        <stop offset="1" stop-color="var(--night)"/>
      </linearGradient>
      <linearGradient id="paperFill" x1="0" y1="0" x2="1" y2="0">
        <stop offset="0" stop-color="var(--paper-shade)"/>
        <stop offset=".12" stop-color="var(--paper)"/>
      </linearGradient>
    </defs>
    <rect class="backdrop__night" width="1200" height="658" fill="url(#nightFill)"/>
    <path class="backdrop__band" fill="var(--brand-blue)"
      d="M0 0 H600 C680 0 715 40 715 110 V560 C715 620 680 658 600 658 H0 Z"/>
    <path class="backdrop__paper" fill="url(#paperFill)"
      d="M0 0 H500 C560 20 590 90 576 170 C560 250 520 290 500 302
         C560 330 615 390 613 463 C610 540 570 610 533 658 H0 Z"/>
  </svg>

  <section class="offer">
    <p class="offer__kicker">Download this</p>
    <h1 class="offer__title">FREE E-Book</h1>
    <p class="pitch__lead">The ONE easy change will make</p>
    <h2 class="pitch__headline">YOUR BUSINESS<br>WEBSITE</h2>
    <p class="pitch__promise">Double your Sales</p>
    <ul class="benefits">
      <li class="benefits__item"><svg class="benefits__tick" viewBox="0 0 36 30"><path d="M2 16 L13 27 L34 3" fill="none" stroke="var(--tick-green)" stroke-width="5" stroke-linecap="round" stroke-linejoin="round"/></svg>GEt more New Customers</li>
      <li class="benefits__item"><svg class="benefits__tick" viewBox="0 0 36 30"><path d="M2 16 L13 27 L34 3" fill="none" stroke="var(--tick-green)" stroke-width="5" stroke-linecap="round" stroke-linejoin="round"/></svg>Buy more</li>
      <li class="benefits__item"><svg class="benefits__tick" viewBox="0 0 36 30"><path d="M2 16 L13 27 L34 3" fill="none" stroke="var(--tick-green)" stroke-width="5" stroke-linecap="round" stroke-linejoin="round"/></svg>Get more reviews</li>
      <li class="benefits__item"><svg class="benefits__tick" viewBox="0 0 36 30"><path d="M2 16 L13 27 L34 3" fill="none" stroke="var(--tick-green)" stroke-width="5" stroke-linecap="round" stroke-linejoin="round"/></svg>Refer more customers</li>
    </ul>
  </section>

  <div class="brand">
    <span class="brand__square"></span>
    <span class="brand__name">Nova<br>Webworks</span>
  </div>

  <div class="hero-art" role="img" aria-label="Isometric illustration of a team building a website layout on a large browser window"></div>

  <p class="visit"><span class="visit__label">Visit:</span> novawebworks.com/website</p>
</main>
</body>
</html>
```